Business card design needed

I need a business card for my private practice. I would like to see the designs that use bright blue and white. I would like to see similar designs as to the card below:
http://blog.printmoss.com/2009/designing-a-business-card-with-pm-kt517-template.html
I would like to see the back of the card have room for appointment times. Thank you.

Industry/Entity Type
Business
Contact Information for Business Card
Tandem Wellbeing & Guidance Services
Fiona Marsh B.Psychology
Registered Psychologist
Building C, Level 3, 14 Wattle Crescent, Canberra, ACT 2601
T: (02) 6248 7315
F: (02) 6248 7390
info@tandemwellbeing.com.au
www.tandemwellbeing.com.au

```html
<!DOCTYPE html>
<html lang="en">
<head>
<meta charset="utf-8">
<title>Business Card Design – Tandem Wellbeing &amp; Guidance Services</title>
<link rel="stylesheet" href="https://fonts.googleapis.com/css2?family=Caladea&family=Crimson+Text:wght@400;700&display=swap">
<style>
  :root {
    --page: #ffffff;
    --brand-blue: #1eb1e8;
    --ink: #111111;
    --card-black: #000000;
    --paper: #ffffff;
    --field-label: #333333;
    --dark-text: #0e1a24;
    --faint-mark: #2a2a2a;
    --shadow: rgba(0, 0, 0, 0.35);
  }
  * { box-sizing: border-box; margin: 0; padding: 0; }
  html, body { width: 1200px; height: 900px; overflow: hidden; background: var(--page); }
  body { position: relative; font-family: "Crimson Text", Georgia, serif; color: var(--ink); }

  .sheet-title {
    position: absolute; top: 89px; left: 0; width: 1200px;
    text-align: center; font-family: "Caladea", Georgia, serif; font-size: 17px;
  }
  .view-label {
    position: absolute; width: 510px; text-align: center;
    font-family: "Caladea", Georgia, serif; font-size: 18px;
  }

  .card {
    position: absolute; width: 510px; height: 288px; overflow: hidden;
    box-shadow: 5px 6px 7px var(--shadow);
  }
  .card--front { background: var(--brand-blue); color: var(--paper); }
  .card--back { background: var(--card-black); }

  .card__mark {
    position: absolute; left: -200px; top: 4px;
    width: 280px; height: 280px; border-radius: 50%;
    background: var(--card-black);
  }
  .card__company {
    position: absolute; left: 88px; top: 90px;
    font-size: 15.5px; letter-spacing: 0.2px; text-transform: uppercase;
    white-space: nowrap;
  }
  .card__details { position: absolute; left: 290px; top: 127px; }
  .card__name { font-size: 15.5px; font-weight: 700; text-transform: uppercase; line-height: 20px; }
  .card__role { font-size: 12px; line-height: 16px; margin-bottom: 10px; }
  .card__contact { font-size: 12px; line-height: 15.6px; font-style: normal; }

  .card--dark-details .card__details { color: var(--dark-text); }
  .card--dark-company .card__company { color: var(--dark-text); }

  .back__mark {
    position: absolute; left: -30px; top: 60px;
    width: 210px; height: 210px; border-radius: 50%;
    background: var(--faint-mark);
  }
  .back__title {
    position: absolute; top: 26px; left: 0; width: 510px; text-align: center;
    color: var(--paper); font-size: 12px; font-weight: 700; letter-spacing: 12px;
  }
  .field {
    position: absolute; left: 30px; width: 451px; height: 29px;
    background: var(--paper); display: flex; align-items: center;
    font-size: 9px; text-transform: uppercase; color: var(--field-label);
  }
  .field span { padding-left: 6px; }
  .field span + span { position: absolute; left: 231px; }
  .field--tall { height: 58px; }
</style>
</head>
<body>
  <h1 class="sheet-title">Business Card Design</h1>

  <section class="card card--front" style="left:76px; top:148px;">
    <div class="card__mark" role="img" aria-label="Large black brand decoration"></div>
    <p class="card__company">Tandem Wellbeing &amp; Guidance Services</p>
    <div class="card__details">
      <p class="card__name">Fiona Marsh</p>
      <p class="card__role">B. Psychology Registered Psychologist</p>
      <address class="card__contact">
        Building C, Level 3, 14 Wattle Crescent<br>
        Canberra, ACT 2601<br>
        Tel:&nbsp; (02) 6248 7315<br>
        Fax: (02) 6248 7390<br>
        info@tandemwellbeing.com.au<br>
        www.tandemwellbeing.com.au
      </address>
    </div>
  </section>
  <p class="view-label" style="left:76px; top:447px;">Front Side View: Option 1</p>

  <section class="card card--front card--dark-details" style="left:614px; top:148px;">
    <div class="card__mark" role="img" aria-label="Large black brand decoration"></div>
    <p class="card__company">Tandem Wellbeing &amp; Guidance Services</p>
    <div class="card__details">
      <p class="card__name">Fiona Marsh</p>
      <p class="card__role">B. Psychology Registered Psychologist</p>
      <address class="card__contact">
        Building C, Level 3, 14 Wattle Crescent<br>
        Canberra, ACT 2601<br>
        Tel:&nbsp; (02) 6248 7315<br>
        Fax: (02) 6248 7390<br>
        info@tandemwellbeing.com.au<br>
        www.tandemwellbeing.com.au
      </address>
    </div>
  </section>
  <p class="view-label" style="left:614px; top:447px;">Front Side View: Option 2</p>

  <section class="card card--front card--dark-company" style="left:76px; top:492px;">
    <div class="card__mark" role="img" aria-label="Large black brand decoration"></div>
    <p class="card__company">Tandem Wellbeing &amp; Guidance Services</p>
    <div class="card__details">
      <p class="card__name">Fiona Marsh</p>
      <p class="card__role">B. Psychology Registered Psychologist</p>
      <address class="card__contact">
        Building C, Level 3, 14 Wattle Crescent<br>
        Canberra, ACT 2601<br>
        Tel:&nbsp; (02) 6248 7315<br>
        Fax: (02) 6248 7390<br>
        info@tandemwellbeing.com.au<br>
        www.tandemwellbeing.com.au
      </address>
    </div>
  </section>
  <p class="view-label" style="left:76px; top:791px;">Front Side View: Option 3</p>

  <section class="card card--back" style="left:614px; top:492px;">
    <div class="back__mark" role="img" aria-label="Faint brand decoration"></div>
    <p class="back__title">APPOINTMENT CARD</p>
    <div class="field" style="top:55px;"><span>Name :</span></div>
    <div class="field" style="top:93px;"><span>Identity No. :</span><span>Race :</span></div>
    <div class="field" style="top:130px;"><span>Sex :</span><span>Birth Date:</span></div>
    <div class="field field--tall" style="top:168px;"><span>Home Address :</span></div>
    <div class="field" style="top:235px;"><span>Contact No. :</span><span>Email :</span></div>
  </section>
  <p class="view-label" style="left:614px; top:791px;">Reverse Side View</p>
</body>
</html>
```